Beard Balm Label

Hi Chaps,

We are needing a label for a new product we are adding to our international beard grooming range.

The design needs to be on a circular label. There will be a top label (that will contain the branding and what the product is) and a bottom label (that will contain the instructions for use and ingredients).

The size of the top label is 75mm in diameter.

The size of the bottom label is 68mm in diameter

It needs to align with our branding from our Beard Oil and Moustache wax product. checkout www.thegrizzledgent.com to get an insight of this.

What needs to be on the label:

- The grizzled gent logo (logo attached)
- Hearthside Beard Balm
- the words "Quality Craftsmanship" "Handmade in Australia" "Protect, Condition, Style"
- "Our all natural Hearthside Beard Balm is made in ABSURDLY small batches and will help you keep even the wildest beard looking sharp, lush and smelling great."
-TheGrizzledGent.com

*all fonts are attached

Information on the bottom label is not important at this stage and will provide the detail after a winner has been chosen.

This project will be open for 5 days.

Any questions, please ask asap.

```html
<!DOCTYPE html>
<html lang="en">
<head>
<meta charset="utf-8">
<title>Hearthside Beard Balm – Label Concepts</title>
<link rel="stylesheet" href="https://fonts.googleapis.com/css2?family=Alegreya+Sans+SC:wght@800;900&family=Bevan&display=swap">
<style>
  :root {
    --page: #ffffff;
    --ink: #141414;
    --cream: #f6efb8;
    --gold: #c8b37c;
    --gold-dark: #a8925c;
    --banner: #efefed;
    --rim-dark: #333333;
    --stitch: #7a4b38;
    --shadow: rgba(0,0,0,0.45);
  }
  html, body {
    margin: 0;
    padding: 0;
    width: 1200px;
    height: 587px;
    overflow: hidden;
    background: var(--page);
  }
  .board {
    position: relative;
    width: 1200px;
    height: 587px;
  }
  .concept-title {
    position: absolute;
    top: 38px;
    margin: 0;
    width: 300px;
    text-align: center;
    font-family: "Alegreya Sans SC", sans-serif;
    font-weight: 900;
    font-size: 28px;
    letter-spacing: 1px;
    color: var(--ink);
  }
  .concept-title--a { left: 183px; }
  .concept-title--b { left: 687px; }
  .labels { position: absolute; inset: 0; }
  .claim-ring {
    font-family: "Alegreya Sans SC", sans-serif;
    font-weight: 900;
    font-size: 15.5px;
    letter-spacing: 0.6px;
    fill: var(--ink);
  }
  .brand-name {
    font-family: "Alegreya Sans SC", sans-serif;
    font-weight: 900;
    font-size: 30px;
    fill: var(--ink);
  }
  .product-top {
    font-family: "Bevan", serif;
    font-size: 22px;
    fill: var(--ink);
  }
  .product-main {
    font-family: "Bevan", serif;
    font-size: 38px;
    fill: var(--ink);
  }
  .blurb, .site {
    font-family: "Alegreya Sans SC", sans-serif;
    font-weight: 800;
    font-size: 14px;
    fill: var(--ink);
  }
</style>
</head>
<body>
<main class="board">
  <h2 class="concept-title concept-title--a">Design A</h2>
  <h2 class="concept-title concept-title--b">Design B</h2>

  <svg class="labels" width="1200" height="587" viewBox="0 0 1200 587" xmlns="http://www.w3.org/2000/svg">
    <defs>
      <radialGradient id="drop-shadow" cx="50%" cy="50%" r="50%">
        <stop offset="0%" stop-color="var(--shadow)"/>
        <stop offset="100%" stop-color="rgba(0,0,0,0)"/>
      </radialGradient>
      <linearGradient id="gold-rim" x1="0" y1="0" x2="0" y2="1">
        <stop offset="0%" stop-color="#d9c796"/>
        <stop offset="100%" stop-color="#bba36a"/>
      </linearGradient>
      <path id="claim-arc" d="M -167.3 60.9 A 178 178 0 1 1 167.3 60.9"/>
      <clipPath id="label-b-face"><circle r="203"/></clipPath>
    </defs>

    <!-- Design A -->
    <g class="label label--a" transform="translate(333 308)">
      <ellipse class="label-shadow" cx="0" cy="232" rx="175" ry="12" fill="url(#drop-shadow)"/>
      <circle class="label-rim" r="201" fill="url(#gold-rim)"/>
      <circle class="label-face" r="191" fill="var(--cream)"/>
      <text class="claim-ring"><textPath href="#claim-arc" startOffset="50%" text-anchor="middle">* Quality Craftsmanship * Handmade in Australia * Protect, Condition, Style*</textPath></text>
      <circle class="brand-dot" cx="0" cy="-108" r="7" fill="var(--ink)"/>
      <text class="brand-name" x="0" y="-66" text-anchor="middle">The Grizzled Gent</text>
      <path class="banner-tails" d="M-172,-6 Q0,16 172,-6 L160,62 Q0,78 -160,62 Z" fill="var(--gold)"/>
      <path class="banner" d="M-152,-22 Q0,-6 152,-22 L152,50 Q0,62 -152,50 Z" fill="var(--banner)"/>
      <text class="product-top" x="0" y="12" text-anchor="middle">HEARTHSIDE</text>
      <text class="product-main" x="0" y="46" text-anchor="middle">BEARD BALM</text>
      <g class="blurb" text-anchor="middle">
        <text x="0" y="87">Our all natural Hearthside Beard Balm</text>
        <text x="0" y="106">is made in ABSURDLY small batches and will help</text>
        <text x="0" y="125">you keep even the wildest beard looking sharp,</text>
        <text x="0" y="144">lush and smelling great</text>
      </g>
      <text class="site" x="0" y="184" text-anchor="middle">TheGrizzledGent.com</text>
    </g>

    <!-- Design B -->
    <g class="label label--b" transform="translate(837 308)">
      <ellipse class="label-shadow" cx="0" cy="232" rx="175" ry="12" fill="url(#drop-shadow)"/>
      <circle class="label-rim" r="211" fill="var(--rim-dark)"/>
      <circle class="label-face" r="203" fill="var(--cream)"/>
      <rect class="footer-band" x="-210" y="166" width="420" height="50" fill="var(--gold)" clip-path="url(#label-b-face)"/>
      <circle class="stitch-line" r="196" fill="none" stroke="var(--stitch)" stroke-width="1.2" stroke-dasharray="3 3"/>
      <text class="claim-ring"><textPath href="#claim-arc" startOffset="50%" text-anchor="middle">* Quality Craftsmanship * Handmade in Australia * Protect, Condition, Style*</textPath></text>
      <circle class="brand-dot" cx="0" cy="-108" r="7" fill="var(--ink)"/>
      <text class="brand-name" x="0" y="-66" text-anchor="middle">The Grizzled Gent</text>
      <path class="banner-tails" d="M-172,-6 Q0,16 172,-6 L160,62 Q0,78 -160,62 Z" fill="var(--gold)"/>
      <path class="banner" d="M-152,-22 Q0,-6 152,-22 L152,50 Q0,62 -152,50 Z" fill="var(--banner)"/>
      <text class="product-top" x="0" y="12" text-anchor="middle">HEARTHSIDE</text>
      <text class="product-main" x="0" y="46" text-anchor="middle">BEARD BALM</text>
      <g class="blurb" text-anchor="middle">
        <text x="0" y="87">Our all natural Hearthside Beard Balm</text>
        <text x="0" y="106">is made in ABSURDLY small batches and will help</text>
        <text x="0" y="125">you keep even the wildest beard looking sharp,</text>
        <text x="0" y="144">lush and smelling great</text>
      </g>
      <text class="site" x="0" y="184" text-anchor="middle">TheGrizzledGent.com</text>
    </g>
  </svg>
</main>
</body>
</html>
```